Email mail merge - not a marketing email, this is an update email sent regularly to our members

HI I need a generic email designed to send out to our members, this is a tri-weekly (monday - updates - Wednesday - updates and Fridays - weekly round up.

we would like it to have within the mail body, 3 interactive, changeable boxes for example "quote of the week', 'top performer' and something else, It would be great if we can remove a box if and when we choose.
Our company is called Vr4lo Amusements or Vr4lo for short.
It needs to be in HTML to fit with our back office software.
We have all the logos for you already which I have included, I have also included our current email header.
our websites are...
vr4lam.cub - This is our members back end site.
vr4lam.com - This is our gaming site.
Please email me on derek@vr4lam.com if you have any queries

Target Market(s)

All of our members - We currently have over 400 but it is growing at an astronomical rate.

Industry/Entity Type

Marketing

Font styles to use
Serif
Decorative
Script

Requirements
Must have
• At least two interactive, changeable boxes/areas that I can put photo's or quotes in to. I would also like some guidelines as to how I change these myself.
• The colours should be inline with our vr4lam.club site.
Nice to have
• This is a positive email update so it needs to look clean and clear but vibrant, we are a unique company that is breaking records and is very successful.
• Our members have the ability and some already are earning vast sums of money.

```html
<!DOCTYPE html>
<html lang="en">
<head>
<meta charset="utf-8">
<title>Vr4lo Club – Member Update</title>
<link rel="stylesheet" href="https://fonts.googleapis.com/css2?family=Questrial&family=Arimo:ital,wght@0,400;0,700;1,700&family=Tinos&display=swap">
<style>
  :root {
    --page-grey: #9ea5a3;
    --card-white: #ffffff;
    --band-grey: #f2f2f2;
    --teal-dark: #0f4e55;
    --teal-deeper: #0a3a3f;
    --night: #0b1f23;
    --aqua: #7fe9d9;
    --gold: #fdb515;
    --ink: #111111;
    --body-grey: #555555;
    --soft-grey: #a9a9a9;
    --logo-grey: #8c8c8c;
    --rule: #c9c9c9;
  }
  * { box-sizing: border-box; margin: 0; padding: 0; }
  html, body { width: 1200px; height: 3688px; overflow: hidden; }
  body {
    position: relative;
    background: var(--page-grey);
    font-family: "Arimo", Arial, sans-serif;
    color: var(--body-grey);
  }
  .abs { position: absolute; }
  .web-view-link {
    top: 32px; left: 0; width: 1200px; text-align: center;
    color: #fff; font-size: 24px;
  }
  .mail-card {
    top: 94px; left: 44px; width: 1112px; height: 3466px;
    background: var(--card-white);
  }
  .brand-wordmark {
    top: 150px; left: 0; width: 1200px; text-align: center;
    font-family: "Questrial", sans-serif; font-size: 118px;
    color: var(--logo-grey); letter-spacing: 4px; line-height: 1;
  }
  .hero-devices {
    top: 360px; left: 250px; width: 780px; height: 570px;
    background: linear-gradient(160deg, #d9dcdc 0%, #3d4548 45%, #15363a 70%, #e8eaea 100%);
    border-radius: 14px;
  }
  .quote-band {
    top: 1112px; left: 44px; width: 1112px; height: 298px;
    background: var(--band-grey);
  }
  .ribbon { top: 1012px; left: 255px; width: 690px; height: 110px; }
  .ribbon-title {
    top: 1022px; left: 300px; width: 600px; height: 80px;
    text-align: center; line-height: 80px;
    font-family: "Questrial", sans-serif; font-size: 52px; color: #fff;
    letter-spacing: 2px;
  }
  .quote-text {
    top: 1205px; left: 150px; width: 900px; text-align: center;
    font-family: "Tinos", serif; font-size: 45px; line-height: 54px; color: #222;
  }
  .quote-rule {
    top: 1344px; left: 494px; width: 212px; height: 6px; background: var(--teal-dark);
  }
  .performer-panel {
    top: 1410px; left: 44px; width: 1112px; height: 710px; background: var(--night);
  }
  .performer-photo {
    top: 1532px; left: 128px; width: 386px; height: 386px; border-radius: 50%;
    background: radial-gradient(circle at 50% 45%, #f3dcc4 0%, #e2b894 45%, #d9c8a8 70%, #f2f2ee 100%);
    border: 10px solid #16363a;
  }
  .performer-heading {
    top: 1462px; left: 573px; font-family: "Questrial", sans-serif;
    font-size: 66px; color: var(--aqua); letter-spacing: 2px; line-height: 1;
  }
  .performer-sub {
    top: 1540px; left: 575px; font-family: "Questrial", sans-serif;
    font-size: 40px; color: #fff; letter-spacing: 1px;
  }
  .performer-name {
    top: 1612px; left: 583px; font-size: 31px; font-weight: 700; font-style: italic;
    color: var(--gold);
  }
  .performer-bio {
    top: 1685px; left: 573px; width: 540px;
    font-size: 28px; line-height: 37.5px; color: #fff;
  }
  .pill-button {
    display: flex; align-items: center; justify-content: center; gap: 26px;
    background: var(--gold); border-radius: 60px;
    color: var(--ink); font-family: "Questrial", sans-serif;
  }
  .pill-button .divider { width: 2px; align-self: stretch; margin: 22% 0; background: rgba(0,0,0,.55); }
  .btn-past { top: 1984px; left: 176px; width: 845px; height: 92px; font-size: 36px; }
  .btn-past .divider, .btn-packages .divider { margin: 20px 0; }
  .membership-title {
    top: 2170px; left: 0; width: 1200px; text-align: center;
    font-family: "Questrial", sans-serif; font-size: 58px; color: var(--ink); letter-spacing: 1px;
  }
  .membership-sub {
    top: 2252px; left: 0; width: 1200px; text-align: center;
    font-family: "Questrial", sans-serif; font-size: 35px; color: #444; letter-spacing: 3px;
  }
  .membership-copy {
    top: 2350px; left: 100px; width: 1000px; text-align: center;
    font-size: 27.5px; line-height: 37px;
  }
  .membership-copy p + p { margin-top: 37px; }
  .btn-packages { top: 2855px; left: 227px; width: 740px; height: 90px; font-size: 36px; }
  .dashed-rule { left: 100px; width: 1000px; border-top: 3px dashed var(--rule); }
  .rule-top { top: 3040px; }
  .rule-bottom { top: 3418px; }
  .office-heading {
    top: 3095px; left: 100px; font-family: "Questrial", sans-serif;
    font-size: 30px; color: var(--soft-grey); letter-spacing: 3px;
  }
  .office-address {
    top: 3175px; left: 100px; width: 460px; font-size: 25px; line-height: 37px; color: var(--soft-grey);
    font-style: normal;
  }
  .office-address strong { color: var(--ink); font-weight: 400; }
  .ent-wordmark {
    top: 3090px; left: 620px; width: 490px; text-align: center;
    font-family: "Questrial", sans-serif; font-size: 76px; color: var(--logo-grey); letter-spacing: 2px;
  }
  .btn-gaming { top: 3256px; left: 621px; width: 486px; height: 66px; font-size: 24px; gap: 20px; }
  .btn-gaming .divider { margin: 14px 0; }
  .social-row {
    top: 3468px; left: 0; width: 1200px; display: flex; justify-content: center; gap: 50px;
  }
  .social-dot { width: 34px; height: 34px; border-radius: 50%; background: #b5b5b5; }
</style>
</head>
<body>
  <div class="abs web-view-link">View this mail in web browser</div>
  <div class="abs mail-card"></div>

  <header>
    <div class="abs brand-wordmark">VR4LO CLUB</div>
    <div class="abs hero-devices" role="img" aria-label="Laptop, tablet and phone showing the members site and gaming site screens"></div>
  </header>

  <section class="quote-box">
    <div class="abs quote-band"></div>
    <svg class="abs ribbon" viewBox="0 0 690 110" aria-hidden="true">
      <polygon points="0,22 70,22 70,102 0,102 24,62" fill="var(--teal-deeper)"/>
      <polygon points="690,22 620,22 620,102 690,102 666,62" fill="var(--teal-deeper)"/>
      <polygon points="45,88 70,102 70,88" fill="#062a2e"/>
      <polygon points="645,88 620,102 620,88" fill="#062a2e"/>
      <rect x="45" y="8" width="600" height="80" fill="var(--teal-dark)"/>
    </svg>
    <h2 class="abs ribbon-title">QUOTES OF THE WEEK</h2>
    <p class="abs quote-text">Lorem isum dolosr sit amet esta di maria nuno valencia ed di mordor.</p>
    <div class="abs quote-rule"></div>
  </section>

  <section class="performer-box">
    <div class="abs performer-panel"></div>
    <div class="abs performer-photo" role="img" aria-label="Portrait photo of the top performer"></div>
    <h2 class="abs performer-heading">TOP PERFORMER</h2>
    <div class="abs performer-sub">OF THE WEEK</div>
    <div class="abs performer-name">Marigold Fenwick</div>
    <p class="abs performer-bio">Nulla vestibulum mauris ac est consequat, quis dapibus diam porta. Suspendisse non ligula lacinia nisi interdum vulputate in sed purus. Quisque eget felis non libero euismod ultricies tristique at nibh. In eros leo, aliquet nec nibh fermentum, faucibus tincidunt dolor. Quisque non lorem vel enim aliquam</p>
    <div class="abs pill-button btn-past">
      <span>VIEW SOME PAST WEEKS TOP PERFORMER</span><span class="divider"></span>
      <svg width="40" height="40" viewBox="0 0 40 40" aria-hidden="true"><circle cx="20" cy="20" r="17" fill="none" stroke="#111" stroke-width="3.5"/><path d="M11 20h16M21 13l7 7-7 7" fill="none" stroke="#111" stroke-width="3.5"/></svg>
    </div>
  </section>

  <section class="membership-box">
    <h2 class="abs membership-title">A GAMOUT OF MEMBERSHIP</h2>
    <div class="abs membership-sub">PACKAGES - TAKE YOUR PICK</div>
    <div class="abs membership-copy">
      <p>Join the VR4LO CLUB Membership and Rewards Program today to start earning income with a new dedicated Gaming and Sport Betting Service directed to the networking industry.</p>
      <p>VR4LO CLUB caters to all levels of users with its range of six rewarding membership plans:, Bronze, Silver, Gold, Ruby, Emerald and Diamond Founder, The Diamond Founder plan is much sought after because there are barely one hundred such memberships on offer worldwide. Nonetheless, each of these plans is a package of delights: earn commissions, share your moneymaking adventure at VR4LO CLUB throughout the membership lifetime, and carry no liability of negative monthly spillovers. It's like you sign a fun contract once you choose us!</p>
    </div>
    <div class="abs pill-button btn-packages">
      <span>CLICK HERE TO CHECK PACKAGES</span><span class="divider"></span>
      <svg width="40" height="40" viewBox="0 0 40 40" aria-hidden="true"><circle cx="20" cy="20" r="17" fill="none" stroke="#111" stroke-width="3.5"/><path d="M11 20h16M21 13l7 7-7 7" fill="none" stroke="#111" stroke-width="3.5"/></svg>
    </div>
  </section>

  <footer>
    <div class="abs dashed-rule rule-top"></div>
    <div class="abs office-heading">REGISTERED OFFICES</div>
    <address class="abs office-address">
      Suite 4, Harbour Court Quayside Lane, Northport, Coastal Territory on the western shore<br>
      Ph:<strong>1300 555 018</strong><br>
      Email: <strong>support@vr4lam.com</strong>
    </address>
    <div class="abs ent-wordmark">VR4LO ENT</div>
    <div class="abs pill-button btn-gaming">
      <span>VISIT OUR GAMING WEBSITE</span><span class="divider"></span>
      <svg width="30" height="30" viewBox="0 0 40 40" aria-hidden="true"><circle cx="20" cy="20" r="17" fill="none" stroke="#111" stroke-width="3.5"/><path d="M11 20h16M21 13l7 7-7 7" fill="none" stroke="#111" stroke-width="3.5"/></svg>
    </div>
    <div class="abs dashed-rule rule-bottom"></div>
    <div class="abs social-row" aria-label="Social links">
      <span class="social-dot"></span><span class="social-dot"></span><span class="social-dot"></span><span class="social-dot"></span><span class="social-dot"></span>
    </div>
  </footer>
</body>
</html>
```